Letterhead for sustainable Last Mile Logistics needed

Dear all,

we are looking for a powerful design for our letterhead. We are a Berlin-based (Germany) logistics company which delivers parcel on the last mile in a sustainable way. Design should communicate: sustainability, integrity, one family, performance-focused, passionate for excellence and customer experience. Please find company logo attached.

Looking forward for

```html
<!DOCTYPE html>
<html lang="en">
<head>
<meta charset="utf-8">
<title>Verdant Route Letterhead</title>
<link href="https://fonts.googleapis.com/css2?family=Arimo:wght@400;700&display=swap" rel="stylesheet">
<style>
  :root {
    --backdrop: #e8e8ea;
    --paper: #ffffff;
    --green-deep: #1f9e48;
    --green-lime: #9dc63b;
    --ink: #3a3a3a;
    --on-green: #ffffff;
  }
  * { box-sizing: border-box; margin: 0; padding: 0; }
  html, body {
    width: 1200px; height: 874px; overflow: hidden;
    background: var(--backdrop);
    font-family: "Arimo", Arial, sans-serif;
  }
  .letterhead {
    position: absolute; left: 306px; top: 22px;
    width: 588px; height: 830px;
    background: var(--paper);
    box-shadow: 0 4px 18px rgba(0,0,0,0.12);
    overflow: hidden;
  }
  .brand {
    position: absolute; left: 50px; top: 58px;
    display: flex; align-items: center; gap: 10px;
  }
  .brand-dot {
    width: 30px; height: 30px; border-radius: 50%;
    background: var(--green-deep);
  }
  .brand-name {
    font-weight: 700; font-size: 22px; letter-spacing: 0.5px;
    color: var(--green-deep); text-transform: uppercase;
  }
  .letter-body {
    position: absolute; left: 128px; top: 170px; width: 410px;
    font-size: 9.2px; line-height: 1.5; color: var(--ink);
  }
  .letter-body p { margin-bottom: 15px; }
  .salutation { margin-bottom: 6px !important; }
  .closing { margin-top: 4px; }
  .signature-mark {
    width: 120px; height: 34px; margin: 6px 0 4px 10px;
    background: linear-gradient(90deg, rgba(31,158,72,0.18), rgba(31,158,72,0.05));
    border-radius: 4px;
  }
  .signer { margin-left: 30px; }
  .footer-band {
    position: absolute; left: 0; bottom: 0; width: 588px; height: 180px;
    background: linear-gradient(160deg, var(--green-lime) 0%, var(--green-deep) 45%, var(--green-deep) 100%);
  }
  .contact {
    position: absolute; right: 34px; top: 680px;
    list-style: none; text-align: right;
    font-size: 10px; line-height: 1.6; color: var(--on-green);
  }
  .contact li { display: flex; justify-content: flex-end; align-items: center; gap: 6px; }
  .contact svg { width: 9px; height: 9px; fill: var(--on-green); }
  .icon-spacer { width: 9px; }
</style>
</head>
<body>
  <main class="letterhead">
    <div class="footer-band" role="img" aria-label="Decorative green footer area"></div>

    <header class="brand">
      <span class="brand-dot"></span>
      <span class="brand-name">Verdant Route</span>
    </header>

    <section class="letter-body">
      <p class="salutation">Dear Sir,</p>
      <p>Lorem ipsum dolor sit amet, consectetur adipiscing elit, sed do eiusmod tempor incididunt ut labore et dolore magna aliqua. Ut enim ad minim veniam, quis nostrud exercitation ullamco laboris nisi ut aliquip ex ea commodo consequat. Duis aute irure dolor in reprehenderit in voluptate velit esse cillum dolore eu fugiat nulla pariatur. Excepteur sint occaecat cupidatat non proident, sunt in culpa qui officia deserunt mollit anim id est laborum. It is a long established fact that a reader will be distracted by the readable content of a page when looking at its layout. The point of using Lorem Ipsum is that it has a more-or-less normal distribution of letters, as opposed to using 'Content here, content here', making it look like readable English.</p>
      <p>But I must explain to you how all this mistaken idea of denouncing pleasure and praising pain was born and I will give you a complete account of the system, and expound the actual teachings of the great explorer of the truth, the master-builder of human happiness. No one rejects, dislikes, or avoids pleasure itself, because it is pleasure, but because those who do not know how to pursue pleasure rationally encounter consequences that are extremely painful. Nor again is there anyone who loves or pursues or desires to obtain pain of itself, because it is pain, but because occasionally circumstances occur in which toil and pain can procure him some great pleasure.</p>
      <p>There are many variations of passages of Lorem Ipsum available, but the majority have suffered alteration in some form, by injected humour, or randomised words which don't look even slightly believable. If you are going to use a passage of Lorem Ipsum, you need to be sure there isn't anything embarrassing hidden in the middle of text. All the Lorem Ipsum generators on the Internet tend to repeat predefined chunks as necessary, making this the first true generator on the Internet.</p>
      <p class="closing">Best Regards</p>
      <div class="signature-mark" role="img" aria-label="Handwritten signature of Martin Hale"></div>
      <p class="signer">Martin Hale</p>
    </section>

    <ul class="contact">
      <li>218 Linden Court<span class="icon-spacer"></span></li>
      <li>Unit 4, Eastfield, Ohio 40117<span class="icon-spacer"></span></li>
      <li>(555) 204 7781
        <svg viewBox="0 0 10 10" aria-hidden="true"><path d="M2 1 L4 1 L4.6 3 L3.4 3.8 C4 5.2 4.8 6 6.2 6.6 L7 5.4 L9 6 L9 8 C9 8.6 8.6 9 8 9 C4.2 9 1 5.8 1 2 C1 1.4 1.4 1 2 1 Z"/></svg>
      </li>
      <li>hello@verdantroutedelivery.com
        <svg viewBox="0 0 10 10" aria-hidden="true"><path d="M0.5 2 L9.5 2 L9.5 8 L0.5 8 Z M1.2 2.6 L5 5.4 L8.8 2.6 Z" fill-rule="evenodd"/></svg>
      </li>
      <li>www.verdantroutedelivery.com
        <svg viewBox="0 0 10 10" aria-hidden="true"><circle cx="5" cy="5" r="4.5"/></svg>
      </li>
    </ul>
  </main>
</body>
</html>
```